Maison Lumet is a premium domestic placement company and a concept of modern etiquette and a manueri

Maison Lumet is a premium domestic placements agency delivering the most professional caliber of domestic professionals to suit even the most demanding, challenging and refined household tasks.

Based in Dubai, Maisone Lumet the world of Maison Lumet is representing the finest.

We genuinely strive to find the best, recruit the right ones and invest our time and resources for that perfect match.

~ Career Nannies ~
~ Etiquette Governesses ~
~ Royal Protocol Attendees ~
~ Formal Palace Personnel ~
~ Official Butler ~
~ World Class Chefs ~
~ Skilled Housekeepers ~
~ Experienced Babynurses ~
~ Domestic Couples ~
~ Professional Laundresses ~
~ Personal Beautician ~
~ Enthusiastic Chauffeurs ~
~ Gourmet Cooks ~

WEB SITE BRIEF:

Style: clean, classy, refined and screaming luxury - you may see sample i like: www.corvellahouseline.com

Colors: I like black and white with a touch of pink (burned sugar more specifically)

Communicate: The images and the web should communicate class and royalty as i will be working with lots of royal families in the Region.

Images selection: this is very important to me has to be with white, black, and perhaps a touch of pink - just to get along with my logo second line.
1. one image may be a palace
2. may be a housekeeper or a butler
3. something etiquette related! or your
PS. Do not limit to those, its just mine idea and also i don't know why but i prefer images without faces - otherwise looks like endorsement and strong personalization to a face that i dont even know

Note: The pictures i have attached are tentative only

Explanation of my web structure: 1 excel page are the web links 2 are the side links, i want them to be like a sliding tips, that you click to see the next 3 social media i will start with

Standards: You may use my logo (middle icon) as a graphic idea and/or whatever you decide i like consistency - in the colors you use, style and all.

General: Easy to navigate

Thank you all in advance & Enjoy the journey

Marguerite

Target Market(s)

- Royal families and VIP's in Middle East
- Families and families with kids
- Mid and High-end segment singles
- Hotels HR departments
- Companies HR departments
- Celebrities ;)

Industry/Entity Type

It Company

Requirements
Must have
• Standards again of design, i don't like mixed style of photography and drawing and sketches all in one. Think there should be an idea in the backbone
Nice to have
• Clean, i like simple things in life
• Elegant and luxury, reliability and care - that should be the message
• on the MAIN side might have one banner that shows my value added package VIP Maison Lumet consisted of the following:
• - priority served contract
• - draw from the best candidates
• - dedicated consultant
• - FREE couture uniform
• - meeting at your choice
• - FREE training from the Maison Lumet advanced manual
• - FREE cooking book
• - Follow up visit/call
Should not have
• 1. variety of styles as said
• 2. images that are used from others in the same industry and styles
• 3. very big letters - prefer smaller fonts
• 4. illustrations that look cheap

```html
<!DOCTYPE html>
<html lang="en">
<head>
<meta charset="utf-8">
<title>Maison Lumet</title>
<link href="https://fonts.googleapis.com/css2?family=Cinzel:wght@400;500&family=Fondamento&family=Tinos&display=swap" rel="stylesheet">
<style>
:root{
  --ink:#111111;
  --paper:#ffffff;
  --bar:#000000;
  --accent-line:#c0601c;
  --bronze:#9b5e2c;
  --muted:#7a7a7a;
  --rule:#d6d6d6;
  --caption:#1d1d20;
  --brand:#333333;
}
*{margin:0;padding:0;box-sizing:border-box}
html,body{width:784px;height:1200px;overflow:hidden;background:var(--paper)}
body{position:relative;font-family:"Tinos",serif;color:var(--ink)}
.brand{position:absolute;top:46px;left:0;width:784px;text-align:center;font-family:"Cinzel",serif;font-weight:400;font-size:17px;letter-spacing:1px;color:var(--brand)}
.main-nav{position:absolute;top:110px;left:15px;width:755px;height:26px;background:var(--bar);border-top:2px solid var(--accent-line);display:flex;justify-content:space-around;align-items:center}
.main-nav a{font-family:"Cinzel",serif;font-size:10px;color:#fff;text-decoration:none;letter-spacing:.5px}
.hero{position:absolute;top:136px;left:15px;width:755px;height:302px;background:linear-gradient(180deg,#6d5a40 0%,#b9a78a 35%,#9a8466 70%,#5c4a35 100%)}
.tiles{position:absolute;top:442px;left:15px;width:755px;height:129px}
.tile{position:absolute;top:0;width:182px;height:129px;border:1px solid #bdbdbd;background:var(--caption)}
.tile .photo{height:92px}
.tile .label{padding:6px 10px 0;font-family:"Cinzel",serif;font-size:10px;color:#fff;line-height:11px}
.intro{position:absolute;top:600px;left:18px;width:750px;font-size:12px;line-height:12.8px}
.learn-more{position:absolute;top:670px;left:19px;font-size:12px;color:var(--bronze);text-decoration:none}
.value{position:absolute;width:322px}
.value h2{font-family:"Fondamento",cursive;font-weight:400;font-size:31px;color:var(--bronze);line-height:36px;margin-bottom:12px}
.value p{font-size:12.3px;line-height:12.8px}
.footer-rule{position:absolute;top:1120px;left:15px;width:755px;border-top:1px solid var(--rule)}
.footer-nav{position:absolute;top:1135px;left:0;width:784px;display:flex;justify-content:center;gap:10px}
.footer-nav a{font-family:"Cinzel",serif;font-size:10.5px;color:var(--muted);text-decoration:none}
</style>
</head>
<body>
<header class="brand">Maison Lumet</header>

<nav class="main-nav">
  <a>About</a><a>Clients</a><a>Candidates</a><a>Services</a><a>VIP &amp; Royal</a><a>Media</a><a>Contact Us</a>
</nav>

<div class="hero" role="img" aria-label="Grand palace staircase with ornate wrought-iron and gilt balustrades leading to an arched doorway with a chandelier"></div>

<section class="tiles">
  <div class="tile" style="left:0">
    <div class="photo" role="img" aria-label="Butler arranging a candlelit dining table" style="background:linear-gradient(135deg,#8a6a4e,#c9a27e 50%,#7e5d44)"></div>
    <div class="label">Every Day Etiquettes<br>&amp; Courtesies</div>
  </div>
  <div class="tile" style="left:191px">
    <div class="photo" role="img" aria-label="Folded napkin and glassware on a formal table setting" style="background:linear-gradient(135deg,#bcb6ad,#e4e0da 50%,#9a8c80)"></div>
    <div class="label">Tabble Setting Etiquettes</div>
  </div>
  <div class="tile" style="left:381px">
    <div class="photo" role="img" aria-label="Two children in formal attire practising manners" style="background:linear-gradient(135deg,#6c7a3a,#b8a98a 55%,#3e3a2c)"></div>
    <div class="label">Etiquettes for Kids</div>
  </div>
  <div class="tile" style="left:571px">
    <div class="photo" role="img" aria-label="Candle light beside an ornamental figurine in the dark" style="background:linear-gradient(135deg,#2a2220,#6a4a34 55%,#7a2a2a)"></div>
    <div class="label">Spiritualiyt for Kids</div>
  </div>
</section>

<p class="intro">At Maisone Lumet, we have a special philosophy of living that is imbedded in what we do and our honest efforts of supporting our industry in setting the standards of household staffing a little bit higher. We have bestowed the name of Maison Lumet not only as a concept, but an attitude towards life and work.&nbsp; Maisone Lumet is a French phrase; in terms of the actual meaning maison means “house” and lumet means “light”. However the concept also encompasses the customs of a good society and breeding, ability to live life well and with intelligent enjoyment, meeting every situation with poise, good manners, and elegance.</p>
<a class="learn-more">learn more</a>

<article class="value" style="top:716px;left:21px"><h2>Respect.</h2><p>At Maison Lumet we care about our fellow human and we do think respecting others is as essential to creating wonderful relationships in life. We respect our Clients and Candidates, our employees and our business collaborators at every level.</p></article>
<article class="value" style="top:716px;left:422px"><h2>Sharing.</h2><p>Emotional and social intelligence, it is important to interact with the society in a savvy and way of sharing and helping others in what they do in life.</p></article>
<article class="value" style="top:836px;left:21px"><h2>Fulfillment.</h2><p>We do believe that in the game of life it is important to have a fulfillment and living our life and its best. This includes security, happiness, love, and confidence.</p></article>
<article class="value" style="top:836px;left:422px"><h2>Human Dignity.</h2><p>At Maison Lumet we value the people for who they are, coming from each and every part of the world and from every upbringing. We do believe that there is a place for growth and education is an important pillar to us.</p></article>
<article class="value" style="top:956px;left:21px"><h2>Manners.</h2><p>Although old or ever looking a romantic concept of a good mannerism and social etiquette, we do believe as saying ‘thank you’ and ‘bon appetite’ are as important to us as understanding our cultural differences and take some time to learn about our neighbor traditions</p></article>
<article class="value" style="top:956px;left:422px"><h2>Philanthropy.</h2><p>Our company is committed to philanthropy and helping a good cause or a group in need. Our company donates in child and parenting related areas</p></article>

<div class="footer-rule"></div>
<nav class="footer-nav">
  <a>About</a><a>Clients</a><a>Candidates</a><a>Services</a><a>VIP &amp; Royal</a><a>Media</a><a>Contact Us</a>
</nav>
</body>
</html>
```